Business Card Design Project - IT Company

Kestrafield Information Technology Solutions
We are an Information Technology Company. We provide computer services to commercial companies. We would like a new card full color front and back with bleeding edge.
We have a logo that you can use or if you want to come up with a new logo that is fine too.
Our colors are mostly Maroon and black but be creative.
Sample Information
Brent R Okafor
4812 W Saguaro Ridge Drive
Suite 410
Phoenix, AZ 85028
O: 602.914.2037
C: 602.468.1290
24/7: 888.914.2037
bokafor@kestrafield.example
www.kestrafield.example
Target Market(s)
Business of all sizes
Industry/Entity Type
Computer
Requirements
Must have
- Bleeding edge
full color on both sides

```html
<!DOCTYPE html>
<html lang="en">
<head>
<meta charset="utf-8">
<title>Kestrafield Business Cards</title>
<link rel="stylesheet" href="https://fonts.googleapis.com/css2?family=Carlito:ital,wght@0,400;0,700;1,400&display=swap">
<style>
  :root {
    --page: #ffffff;
    --card-edge: #3a3a3a;
    --ink: #333333;
    --white: #ffffff;
    --red-main: #e1262a;
    --red-deep: #c91f26;
    --pink-deep: #cf3a88;
    --pink-light: #f98bc2;
    --pink-edge: #d64b97;
    --icon: #8a8a8a;
  }
  * { margin: 0; padding: 0; box-sizing: border-box; }
  html, body {
    width: 1200px; height: 1114px; overflow: hidden;
    background: var(--page);
    font-family: "Carlito", "Calibri", Arial, sans-serif;
    color: var(--ink);
  }
  .canvas { position: relative; width: 1200px; height: 1114px; }

  .card {
    position: absolute;
    left: 222px;
    background: var(--white);
    border: 2px solid var(--card-edge);
  }
  .card--red  { top: 31px;  width: 816px; height: 484px; --band-top: 46px; --band-h: 275px; --name-top: 18px; --logo-top: 140px; }
  .card--pink { top: 532px; width: 825px; height: 497px; --band-top: 24px; --band-h: 304px; --name-top: 38px; --logo-top: 166px; }

  .band {
    position: absolute; left: 0; right: 0;
    top: var(--band-top); height: var(--band-h);
    color: var(--white);
  }
  .card--red .band {
    background: linear-gradient(120deg, var(--red-main) 0%, var(--red-main) 55%, var(--red-deep) 100%);
  }
  .card--pink .band {
    background: radial-gradient(ellipse 45% 120% at 55% 40%, var(--pink-light) 0%, rgba(249,139,194,0) 100%),
                linear-gradient(90deg, var(--pink-deep) 0%, #e461a5 50%, var(--pink-edge) 100%);
  }

  .contact-head {
    position: absolute; right: 22px; top: var(--name-top);
    text-align: right;
  }
  .contact-head .name { font-weight: 700; font-size: 22px; line-height: 26px; }
  .contact-head .web {
    font-style: italic; font-size: 19px; line-height: 26px; letter-spacing: 0.8px;
  }

  .brand { position: absolute; left: 58px; top: var(--logo-top); }
  .brand .wordmark {
    font-weight: 700; font-size: 70px; line-height: 70px; letter-spacing: -0.5px;
    color: var(--white);
  }
  .brand .tagline { font-size: 15px; line-height: 18px; margin-top: 4px; }

  .details {
    position: absolute; left: 0; right: 0;
    top: calc(var(--band-top) + var(--band-h)); bottom: 0;
    font-size: 19px; line-height: 26px;
  }
  .address { position: absolute; left: 86px; top: 40px; font-style: normal; }
  .phones { position: absolute; right: 22px; top: 40px; text-align: right; }
  .phones b { font-weight: 700; }
  .icon { fill: none; stroke: var(--icon); stroke-width: 1.6; }
  .icon--mail { position: absolute; left: 56px; top: 70px; }
  .icon--phone { vertical-align: -3px; margin-right: 8px; }
</style>
</head>
<body>
<main class="canvas">

  <section class="card card--red" aria-label="Business card, red version">
    <div class="band">
      <div class="contact-head">
        <p class="name">Brent R Okafor</p>
        <p class="web">bokafor@kestrafield.example</p>
        <p class="web">www.kestrafield.example</p>
      </div>
      <div class="brand">
        <p class="wordmark">Kestrafield</p>
        <p class="tagline">Information Technology Solutions</p>
      </div>
    </div>
    <div class="details">
      <svg class="icon icon--mail" width="22" height="16" viewBox="0 0 22 16" aria-hidden="true"><rect x="1" y="1" width="20" height="14"/><path d="M1 1 L11 9 L21 1"/></svg>
      <address class="address">
        4812 W Saguaro Ridge Drive<br>Suite 410<br>Phoenix, AZ 85028
      </address>
      <p class="phones"><b>O:</b> 602.914.2037<br><svg class="icon icon--phone" width="18" height="18" viewBox="0 0 20 20" aria-hidden="true"><circle cx="10" cy="10" r="8.5"/><path d="M7 5.5 L8.5 8 L7.5 9 Q9 12 11 12.5 L12 11.5 L14.5 13 L13 14.5 Q8 14 5.5 7 Z"/></svg><b>C:</b> 602.468.1290<br><b>24/7:</b> 888.914.2037</p>
    </div>
  </section>

  <section class="card card--pink" aria-label="Business card, pink version">
    <div class="band">
      <div class="contact-head">
        <p class="name">Brent R Okafor</p>
        <p class="web">bokafor@kestrafield.example</p>
        <p class="web">www.kestrafield.example</p>
      </div>
      <div class="brand">
        <p class="wordmark">Kestrafield</p>
        <p class="tagline">Information Technology Solutions</p>
      </div>
    </div>
    <div class="details">
      <svg class="icon icon--mail" width="22" height="16" viewBox="0 0 22 16" aria-hidden="true"><rect x="1" y="1" width="20" height="14"/><path d="M1 1 L11 9 L21 1"/></svg>
      <address class="address">
        4812 W Saguaro Ridge Drive<br>Suite 410<br>Phoenix, AZ 85028
      </address>
      <p class="phones"><b>O:</b> 602.914.2037<br><svg class="icon icon--phone" width="18" height="18" viewBox="0 0 20 20" aria-hidden="true"><circle cx="10" cy="10" r="8.5"/><path d="M7 5.5 L8.5 8 L7.5 9 Q9 12 11 12.5 L12 11.5 L14.5 13 L13 14.5 Q8 14 5.5 7 Z"/></svg><b>C:</b> 602.468.1290<br><b>24/7:</b> 888.914.2037</p>
    </div>
  </section>

</main>
</body>
</html>
```